New Facebook Banner

Hi
We are operating Ramen shop in Australia.(http://mizunokobowls.com)
I want to create new design for our Facebook banner and title is "Free Ramen on your Birthday".
Sample attached is our existing banner design. We would like to make it more modern and sophisticated.
We are so looking forward to seeing your design for our free ramen promotion.

https://www.facebook.com/mizunokobowls/

Industry/Entity Type

Japanese Restaurant

Font styles to use
Sans Serif

```html
<!DOCTYPE html>
<html lang="en">
<head>
<meta charset="utf-8">
<title>Mizunoko – Free Ramen on Your Birthday</title>
<link href="https://fonts.googleapis.com/css2?family=Bebas+Neue&display=swap" rel="stylesheet">
<style>
  :root {
    --page: #e4e4e4;
    --sun: #f4c836;
    --white: #ffffff;
    --sky: #1e8fd6;
    --ink: #23348f;
    --chili: #d7262b;
    --broth-dark: #b88a55;
    --broth-light: #eadbc4;
  }
  html, body {
    margin: 0;
    width: 1200px;
    height: 798px;
    overflow: hidden;
    background: var(--page);
  }
  .banner {
    position: absolute;
    left: 0;
    top: 175px;
    width: 1200px;
    height: 447px;
    background: var(--sun);
    overflow: hidden;
    font-family: "Bebas Neue", "Arial Narrow", sans-serif;
  }
  .banner__photo {
    position: absolute;
    left: 0;
    top: 0;
    width: 600px;
    height: 447px;
  }
  .frame__top, .frame__bottom {
    position: absolute;
    left: 520px;
    width: 655px;
    height: 5px;
    background: linear-gradient(to right, rgba(255,255,255,0), var(--white) 20%);
  }
  .frame__top { top: 25px; }
  .frame__bottom { top: 408px; }
  .frame__side {
    position: absolute;
    left: 1170px;
    top: 25px;
    width: 5px;
    height: 388px;
    background: var(--white);
  }
  .brand {
    position: absolute;
    left: 852px;
    top: 78px;
    display: flex;
    align-items: center;
    gap: 10px;
  }
  .brand__dot {
    width: 30px;
    height: 30px;
    border-radius: 50%;
    background: var(--chili);
  }
  .brand__name {
    font-size: 46px;
    line-height: 1;
    color: var(--ink);
    letter-spacing: 1px;
    padding-top: 4px;
  }
  .headline {
    position: absolute;
    right: 67px;
    top: 170px;
    margin: 0;
    text-align: right;
    color: var(--white);
    font-weight: 400;
    text-shadow: -5px 4px 0 var(--sky);
  }
  .headline__main {
    display: block;
    font-size: 108px;
    line-height: 1;
    letter-spacing: 1px;
  }
  .headline__sub {
    display: block;
    font-size: 67px;
    line-height: 1;
    margin-top: 22px;
    letter-spacing: 0.5px;
  }
</style>
</head>
<body>
  <section class="banner">
    <svg class="banner__photo" viewBox="0 0 600 447" role="img" aria-label="Photo of a bowl of shoyu ramen topped with chashu pork slices, spring onion and bamboo shoots">
      <defs>
        <linearGradient id="broth" x1="0" y1="0" x2="1" y2="1">
          <stop offset="0" stop-color="var(--broth-dark)"/>
          <stop offset="0.6" stop-color="var(--broth-light)"/>
          <stop offset="1" stop-color="#d9c2a0"/>
        </linearGradient>
      </defs>
      <path d="M0 0 H472 C560 60 600 180 585 260 C578 330 565 400 547 447 H0 Z" fill="url(#broth)"/>
    </svg>

    <div class="frame__top"></div>
    <div class="frame__bottom"></div>
    <div class="frame__side"></div>

    <div class="brand">
      <span class="brand__dot"></span>
      <span class="brand__name">Mizunoko</span>
    </div>

    <h1 class="headline">
      <span class="headline__main">Free Ramen</span>
      <span class="headline__sub">On Your Birthday!</span>
    </h1>
  </section>
</body>
</html>
```